Business card for law firm

Need business card for new law firm. Think confident, authoritative, conservative, but not stuffy or old-fashioned.

Contact Information for Business Card

Content for card - logo (uploaded), plus the following:

Paul Wexbury (larger font)
Managing Partner (larger font, but not as large as name)
Level 9, 41 Tansy Lane
Sydney NSW 2000
Main Tel 02 7346 2190
Direct Tel 02 6273 4415
Email paul@qvlegal.com.au
www.qvlegal.com.au

Letterhead design should include logo plus:
Level 9, 41 Tansy Lane
Sydney NSW 2000
Tel 02 6273 4415
www.qvlegal.com.au

```html
<!DOCTYPE html>
<html lang="en">
<head>
<meta charset="utf-8">
<title>Quillvale Legal – Business Card</title>
<link href="https://fonts.googleapis.com/css2?family=Cormorant+Garamond:wght@600&family=IBM+Plex+Sans:wght@300;400&display=swap" rel="stylesheet">
<style>
  :root {
    --page: #ffffff;
    --card: #f0f0f2;
    --navy: #1e2654;
    --gold: #7d6240;
    --ink: #111111;
    --address: #2b2c48;
  }
  html, body {
    margin: 0;
    width: 1200px;
    height: 1200px;
    overflow: hidden;
    background: var(--page);
  }
  .card {
    position: absolute;
    left: 75px;
    top: 300px;
    width: 1050px;
    height: 600px;
    background: var(--card);
    overflow: hidden;
  }
  .card-shapes {
    position: absolute;
    inset: 0;
  }
  .firm-name {
    position: absolute;
    left: 57px;
    top: 338px;
    width: 298px;
    margin: 0;
    font-family: "Cormorant Garamond", serif;
    font-weight: 600;
    color: var(--ink);
    text-align: justify;
    text-align-last: justify;
  }
  .firm-name .line { display: block; }
  .firm-name .primary { font-size: 50px; line-height: 50px; letter-spacing: 1px; }
  .firm-name .secondary { font-size: 22px; line-height: 28px; }
  .firm-rule {
    position: absolute;
    left: 57px;
    top: 422px;
    width: 298px;
    height: 3px;
    background: var(--navy);
  }
  .address {
    position: absolute;
    left: 57px;
    top: 438px;
    margin: 0;
    font-family: "IBM Plex Sans", sans-serif;
    font-weight: 300;
    font-size: 28px;
    line-height: 35px;
    color: var(--address);
    font-style: normal;
  }
  .person {
    position: absolute;
    right: 52px;
    top: 124px;
    text-align: right;
  }
  .person-name {
    margin: 0;
    font-family: "Cormorant Garamond", serif;
    font-weight: 600;
    font-size: 52px;
    line-height: 52px;
    color: var(--gold);
  }
  .person-title {
    margin: 0;
    font-family: "IBM Plex Sans", sans-serif;
    font-weight: 300;
    font-size: 35px;
    line-height: 42px;
    color: var(--gold);
  }
  .person-rule {
    position: absolute;
    left: 609px;
    top: 226px;
    width: 408px;
    height: 2px;
    background: var(--gold);
  }
  .contacts {
    position: absolute;
    right: 55px;
    top: 240px;
    margin: 0;
    padding: 0;
    list-style: none;
    font-family: "IBM Plex Sans", sans-serif;
    font-weight: 300;
    font-size: 27px;
    line-height: 42px;
    color: var(--gold);
  }
  .contacts li {
    display: flex;
    justify-content: flex-end;
    align-items: center;
    gap: 16px;
  }
  .contacts svg { width: 30px; height: 30px; flex: none; }
</style>
</head>
<body>
  <main class="card">
    <svg class="card-shapes" viewBox="0 0 1050 600" width="1050" height="600" aria-hidden="true">
      <polygon points="0,0 373,0 0,357" fill="var(--navy)"/>
      <line x1="641" y1="0" x2="305" y2="326" stroke="var(--gold)" stroke-width="1.5"/>
      <line x1="612" y1="407" x2="413" y2="602" stroke="var(--navy)" stroke-width="1.5"/>
    </svg>

    <h1 class="firm-name">
      <span class="line primary">QUILLVALE</span>
      <span class="line secondary">LEGAL</span>
    </h1>
    <div class="firm-rule"></div>

    <address class="address">
      Level 9, 41 Tansy Lane<br>
      Sydney NSW 2000<br>
      Main: 02 7346 2190
    </address>

    <div class="person">
      <p class="person-name">PAUL WEXBURY</p>
      <p class="person-title">Managing Partner</p>
    </div>
    <div class="person-rule"></div>

    <ul class="contacts">
      <li>Direct: 02 6273 4415
        <svg viewBox="0 0 24 24" aria-hidden="true"><path fill="var(--gold)" d="M6.6 2.5l2.6 3.6c.4.5.3 1.2-.1 1.6L7.6 9.2c1 2.6 3 4.9 5.5 6.2l1.6-1.5c.4-.4 1.1-.5 1.6-.1l3.5 2.6c.5.4.6 1.1.2 1.6l-1.8 2.3c-.5.6-1.3.8-2 .5C9.7 18.6 5 13.6 3.1 7c-.2-.7 0-1.5.6-2l1.9-1.7c.3-.3.7-.4 1-.8z"/></svg>
      </li>
      <li>paul@qvlegal.com.au
        <svg viewBox="0 0 24 24" aria-hidden="true"><rect x="1" y="5" width="22" height="15" fill="var(--gold)"/><path d="M1 5l11 8 11-8" fill="none" stroke="var(--card)" stroke-width="2"/></svg>
      </li>
      <li>www.qvlegal.com.au
        <svg viewBox="0 0 24 24" aria-hidden="true"><g fill="none" stroke="var(--gold)" stroke-width="2"><circle cx="12" cy="12" r="10"/><ellipse cx="12" cy="12" rx="4.5" ry="10"/><path d="M2 12h20M4 7h16M4 17h16"/></g></svg>
      </li>
    </ul>
  </main>
</body>
</html>
```